Cutting Costs Quickly - A Weekend Money Plan

Nonfiction book about how to save on insurance. Almost one hundred measures and examples to reduce ones insurance costs.

Target Market(s)

Men/Women between 18 and 50

Industry/Entity Type

Insurance

```html
<!DOCTYPE html>
<html lang="en">
<head>
<meta charset="utf-8">
<title>Cutting Costs Quickly – A Weekend Money Plan</title>
<link rel="stylesheet" href="https://fonts.googleapis.com/css2?family=Roboto+Condensed:wght@700&family=Playfair+Display:ital,wght@1,700&display=swap">
<style>
  :root {
    --paper: #ffffff;
    --cover-black: #231f20;
    --title-white: #ffffff;
    --subtitle-olive: #848e57;
    --bill-light: #e4e8cf;
    --bill-mid: #a9b785;
    --bill-dark: #6f7f45;
  }
  html, body {
    margin: 0;
    padding: 0;
    overflow: hidden;
    background: var(--paper);
  }
  .cover {
    position: relative;
    width: 927px;
    height: 1200px;
    background: var(--paper);
    overflow: hidden;
  }
  .cover__panel {
    position: absolute;
    left: 42px;
    top: 90px;
    width: 862px;
    height: 1070px;
    background: var(--cover-black);
  }
  .cover__title {
    position: absolute;
    left: 42px;
    top: 122px;
    width: 862px;
    margin: 0;
    text-align: center;
    font-family: "Roboto Condensed", "Arial Narrow", sans-serif;
    font-weight: 700;
    font-size: 116px;
    line-height: 142px;
    letter-spacing: 1px;
    text-transform: uppercase;
    color: var(--title-white);
  }
  .cover__title span { display: block; }
  .cover__money {
    position: absolute;
    left: 15px;
    top: 540px;
    width: 333px;
    height: 620px;
    background: linear-gradient(170deg, var(--bill-light) 0%, var(--bill-mid) 55%, var(--bill-dark) 100%);
    border-radius: 6px;
  }
  .cover__subtitle {
    position: absolute;
    left: 365px;
    top: 700px;
    width: 500px;
    margin: 0;
    text-align: center;
    font-family: "Playfair Display", Georgia, serif;
    font-style: italic;
    font-weight: 700;
    font-size: 92px;
    line-height: 108px;
    color: var(--subtitle-olive);
  }
  .cover__subtitle span { display: block; }
</style>
</head>
<body>
  <main class="cover">
    <div class="cover__panel"></div>
    <h1 class="cover__title">
      <span>Cutting</span>
      <span>Costs</span>
      <span>Quickly</span>
    </h1>
    <div class="cover__money" role="img" aria-label="Illustration of banknotes fluttering down onto a tall stack of banded dollar bills"></div>
    <p class="cover__subtitle">
      <span>A Weekend</span>
      <span>Money</span>
      <span>Plan</span>
    </p>
  </main>
</body>
</html>
```